T&R Custom Homes and Remodeling Flyer

We need a new double sided flyer that showcases our service.
Our website is http://trhomesbuild.example/
Please use the information on http://trhomesbuild.example/about-us/ for the information in the flyer.
This handout will be used to give to our potential customers and needs to show the complete story of who we are and the services we provide. I have also attached pictures of project we have completed that should be used for the flyer.
Any other pictures can be taken from our photo gallery on the website.

Target Market(s)

Clients who want a custom home or remodel

Industry/Entity Type

Construction

Font styles to use
Serif

Requirements
Must have
• Prominent logo
• Pictures of completed projects
• Tri-fold design- eps file is attached for this
Nice to have
• Manly colors
• If you can find a tasteful way to add the picture of the owners that is great, but it should be small and is not necessary.
Should not have
• Pink/girly touches

```html
<!DOCTYPE html>
<html lang="en">
<head>
<meta charset="utf-8">
<title>T&amp;R Custom Homes and Remodeling – Tri-fold Inside</title>
<link rel="stylesheet" href="https://fonts.googleapis.com/css2?family=Open+Sans:wght@400;600&display=swap">
<style>
  :root {
    --page-bg: #e4e4e4;
    --paper: #ffffff;
    --teal: #2f9e98;
    --charcoal: #474747;
    --body-text: #555a5e;
  }
  * { box-sizing: border-box; margin: 0; padding: 0; }
  html, body { width: 1200px; height: 870px; overflow: hidden; background: var(--page-bg); }
  body { font-family: "Open Sans", Arial, sans-serif; }

  .brochure {
    position: absolute; left: 50px; top: 10px;
    width: 1100px; height: 850px;
    background: var(--paper);
    box-shadow: 0 6px 18px rgba(0,0,0,.18);
    overflow: hidden;
  }

  /* Left text panel */
  .panel-story {
    position: absolute; left: 0; top: 0; width: 367px; height: 850px;
    background: var(--paper);
  }
  .section-title {
    position: absolute; left: 24px;
    font-size: 21px; font-weight: 400; color: var(--teal); line-height: 1.2;
  }
  .section-copy {
    position: absolute; left: 24px; width: 324px;
    font-size: 13px; line-height: 1.4; color: var(--body-text);
    text-align: justify;
  }
  .title-about { top: 28px; }
  .copy-about { top: 60px; }
  .title-values { top: 394px; }
  .copy-values { top: 426px; }

  .photo { position: absolute; }
  .photo-house { left: 0; top: 205px; width: 367px; height: 176px;
    background: linear-gradient(180deg, #c9d6e2 0%, #b9a08c 45%, #9a6f58 62%, #4f7a3a 82%, #3f6a2e 100%); }
  .photo-hallway { left: 0; top: 612px; width: 367px; height: 238px;
    background: linear-gradient(160deg, #efe9e1 0%, #cfc3b3 40%, #8a6a4c 75%, #5a3e2a 100%); }

  /* Photo collage over middle and right panels */
  .panel-gallery {
    position: absolute; left: 367px; top: 0; width: 733px; height: 850px;
    background: var(--charcoal);
  }
  .photo-kitchen { left: 0; top: 0; width: 400px; height: 300px;
    background: linear-gradient(170deg, #d8cbb6 0%, #5b4535 40%, #e9e4da 62%, #3e2d22 100%); }
  .photo-entry-door { left: 410px; top: 0; width: 323px; height: 370px;
    background: linear-gradient(180deg, #a88c6c 0%, #6b4423 35%, #8d5a30 65%, #9a9690 100%); }
  .photo-dining { left: 0; top: 310px; width: 240px; height: 175px;
    background: linear-gradient(180deg, #6e6656 0%, #cfc7b4 45%, #efeae0 70%, #6a4628 100%); }
  .photo-staircase { left: 250px; top: 310px; width: 150px; height: 175px;
    background: linear-gradient(150deg, #e8e2d6 0%, #9c8772 50%, #4a3526 100%); }
  .photo-bathroom { left: 0; top: 495px; width: 290px; height: 355px;
    background: linear-gradient(170deg, #d9d0c0 0%, #3a2a22 35%, #c9b8a0 70%, #b5a28a 100%); }
  .photo-dark-hall { left: 300px; top: 495px; width: 100px; height: 355px;
    background: linear-gradient(180deg, #1e2a38 0%, #2c3b4c 60%, #142030 100%); }
  .photo-tiled-kitchen { left: 410px; top: 380px; width: 323px; height: 470px;
    background: linear-gradient(165deg, #3a3634 0%, #b7a58c 30%, #6a4a34 60%, #9a3a30 85%, #5a3a28 100%); }

  .footer-band { position: absolute; left: 0; bottom: 0; width: 1100px; height: 130px; }
</style>
</head>
<body>
  <div class="brochure">

    <section class="panel-story">
      <h2 class="section-title title-about">About us</h2>
      <p class="section-copy copy-about">With more than 20 years combined experience in construction, T&amp;R maintains the absolute highest levels of quality, material, workmanship, and service in each and every project we build. A reputation is only as great as the last referral and we understand that the future of our business relies upon satisfied customers.</p>

      <div class="photo photo-house" role="img" aria-label="Photo of a large brick custom home with a green lawn"></div>

      <h2 class="section-title title-values">Quality, Reliability, Value</h2>
      <p class="section-copy copy-values">We take the time to fully understand our customer's expectations. Customer service is more than just a trendy marketing theme, it is the underlying philosophy in everything we do and our home buyers reap the benefits of this philosophy. T&amp;R is committed to building quality homes with meticulous craftsmanship, custom designs, and thoughtful touches that add to the homeowners' quality of life.</p>

      <div class="photo photo-hallway" role="img" aria-label="Photo of a bright arched entry hall with a staircase and wood floors"></div>
    </section>

    <section class="panel-gallery">
      <div class="photo photo-kitchen" role="img" aria-label="Photo of a kitchen with dark cabinets and a white island"></div>
      <div class="photo photo-entry-door" role="img" aria-label="Photo of a wooden front door with glass panels in a brick archway"></div>
      <div class="photo photo-dining" role="img" aria-label="Photo of a dining room with wainscoting and a chandelier"></div>
      <div class="photo photo-staircase" role="img" aria-label="Photo of a wooden staircase"></div>
      <div class="photo photo-bathroom" role="img" aria-label="Photo of a bathroom with dark vanity cabinets"></div>
      <div class="photo photo-dark-hall" role="img" aria-label="Photo of a dark blue hallway"></div>
      <div class="photo photo-tiled-kitchen" role="img" aria-label="Photo of a kitchen with a patterned tile backsplash and bar stools"></div>
    </section>

    <svg class="footer-band" viewBox="0 0 1100 130" preserveAspectRatio="none" aria-hidden="true">
      <defs>
        <clipPath id="clip-story"><rect x="0" y="0" width="367" height="130"/></clipPath>
        <clipPath id="clip-gallery"><rect x="367" y="0" width="733" height="130"/></clipPath>
      </defs>
      <path clip-path="url(#clip-gallery)" fill="var(--charcoal)"
            d="M0,74 C380,66 720,54 1100,2 L1100,130 L0,130 Z"/>
      <path clip-path="url(#clip-story)" fill="var(--paper)"
            d="M0,108 C380,100 720,86 1100,38 L1100,130 L0,130 Z"/>
      <path fill="var(--teal)"
            d="M0,88 C380,80 720,66 1100,16 L1100,38 C720,86 380,100 0,108 Z"/>
    </svg>

  </div>
</body>
</html>
```